Walk Bold Stay Kind Ebook and Print book cover

I need a professional, eye catching cover that will stand out. The title of the book is "Walk Bold Stay Kind: 47 Quiet Rules For Calm and Wonder" It is a self-help personal transformation book by author Dale Ormsby. The cover will be on both print and ebook covers. I want something that is similar yet different to best-selling books in the genre, nothing too boring. A blue background might work, but it isn't a requirement. I'm open to other colors as long as it's powerful, professional, and screams "Buy me because this book is going to change your life!"
Updates

So far, 3 designs (3 of the 4 star rated designs) are in contention, but they all can be improved. I think the book cover should best convey "thinking smart" in a dynamic way. I'll run another poll in a day or so when I get additional designs I like. Added Thursday, May 4, 2017

Based on current designs, I wanted to provide additional guidance. The title and image should pop and be clearly visible at a distance as a thumbnail. Also, I'm wanting something bold and creative but not too confusing. I currently have a couple solid designs that are in contention to win, but I have another 7 days left for the project. I extended it to 10 days from the initial 5. I'll include several more polls for my followers and will likely pick the top ranking design based off the series of polls and will be eliminating lower ranking designs with each new poll and set of promising designs that come in. Finally, I may ask to see what the back will look like on the print version since I'll need both the Lumora and print (5" by 8") designs. Added Saturday, May 6, 2017

It's been recommended by some that I should have my own picture on the cover. I'm not completely convinced, but I would like to see some additional designs that incorporate my photo (touched up to remove the shine from my forehead and the label brand name removed from the t-shire) into a cover design. I have several good designs coming in, so typeset and professional looking font is extremely important. Blue is also preferred but not required. I've attached the photo on the brief for those who want to submit a design with that photo. Added Saturday, May 6, 2017

Target Market(s)

Working age adults seeking personal transformation and self improvement.

Industry/Entity Type

Motivation

Requirements
Must have
• Creativity. Eye catching. Striking. Contrast. Looks good close up and as a thumbnail at a distance. Font should be easy to read and pop from the cover along with the design.
Nice to have
• Powerful image placement. Play up the "Walk Bold" aspect of the title. Perhaps even contrasting someone who's thinking "Hard." Here are a few examples of intriguing covers (though not necessarily related to the genre) I like mainly for aesthetics and creativity. https://www.shopvale.com/dp/Q71MRT2KWD/ https://www.shopvale.com/dp/Q34PLN8XEA
• https://www.shopvale.com/dp/Q925GHV3TC/
• https://www.shopvale.com/dp/Q48DJW6RZB/
• (the font is a little poor in the last one but the image is evoking)
Should not have
• Ugly, tacky, or hard to read fonts. A simple photo with text on top. A simple background with words. Confusing images. Designs with no additional stock image purchase requirements will be given preference over those that do. I've seen a lot of balloons and light bulbs. I'm not saying you can't include them in the design, but if you want to stand out, try to find something more creative that expresses the concept of the title.

```html
<!DOCTYPE html>
<html lang="en">
<head>
<meta charset="utf-8">
<title>Walk Bold Stay Kind – Print Cover Spread</title>
<link rel="stylesheet" href="https://fonts.googleapis.com/css2?family=Oswald:wght@600&family=PT+Sans+Narrow:wght@700&family=Arimo:wght@400;700&display=swap">
<style>
  :root {
    --space-deep: #04070f;
    --space-blue: #0b2a66;
    --space-glow: #2f6fd6;
    --nebula-dark: #0b0302;
    --nebula-red: #a51c08;
    --spine-cream: #f7f3c6;
    --ink: #111111;
    --white: #ffffff;
    --title-yellow: #f6f000;
    --photo-glow: #f4f9fe;
    --photo-light: #cfe4f7;
    --photo-mid: #6fa8e0;
    --photo-edge: #3f86d0;
    --photo-deep: #15509e;
  }
  * { margin: 0; padding: 0; box-sizing: border-box; }
  html, body { width: 1200px; height: 776px; overflow: hidden; background: #ffffff; }
  .spread { position: relative; width: 1200px; height: 776px; overflow: hidden; }

  /* Back cover */
  .back-cover { position: absolute; left: 0; top: 0; width: 580px; height: 776px; }
  .back-art {
    position: absolute; inset: 0;
    background:
      radial-gradient(ellipse 70px 40px at 450px 40px, rgba(190,40,12,0.75), transparent 75%),
      radial-gradient(ellipse 110px 55px at 360px 120px, rgba(180,32,10,0.8), transparent 75%),
      radial-gradient(ellipse 130px 60px at 250px 200px, rgba(165,28,8,0.75), transparent 75%),
      radial-gradient(ellipse 140px 70px at 120px 280px, rgba(150,26,8,0.7), transparent 75%),
      radial-gradient(ellipse 70px 150px at 0px 380px, rgba(175,40,10,0.8), transparent 75%),
      var(--nebula-dark);
  }
  .back-blurb {
    position: absolute; left: 248px; top: 598px;
    font-family: "Arimo", Arial, sans-serif; color: var(--white);
    font-size: 23.5px; line-height: 26.5px;
  }
  .back-blurb h2 {
    font-size: 23.5px; font-weight: 700; text-decoration: underline;
    text-underline-offset: 3px; line-height: 26.5px;
  }

  /* Spine */
  .spine {
    position: absolute; left: 580px; top: 0; width: 38px; height: 776px;
    background: var(--spine-cream);
  }
  .spine-text {
    position: absolute; left: 9px; top: 22px;
    writing-mode: vertical-rl;
    font-family: "Arimo", Arial, sans-serif; font-size: 16.5px; color: var(--ink);
    white-space: nowrap;
  }
  .spine-author { top: 612px; }

  /* Front cover */
  .front-cover { position: absolute; left: 618px; top: 0; width: 582px; height: 776px; }
  .front-art {
    position: absolute; inset: 0;
    background:
      radial-gradient(ellipse 40% 50% at 100% 60%, rgba(47,111,214,0.85), transparent 70%),
      radial-gradient(ellipse 80% 40% at 50% 100%, rgba(11,42,102,0.9), transparent 70%),
      linear-gradient(160deg, var(--space-deep) 0%, #081636 55%, var(--space-blue) 100%);
  }
  .front-title {
    position: absolute; left: 0; width: 582px; top: 72px; text-align: center;
    font-family: "Oswald", "Arial Narrow", sans-serif; font-weight: 600;
    color: var(--white); font-size: 72px; line-height: 86px; letter-spacing: 0.5px;
    transform: scaleX(0.92);
  }
  .front-title span { display: block; }
  .front-subtitle {
    position: absolute; left: 0; width: 582px; top: 250px; text-align: center;
    font-family: "PT Sans Narrow", "Arial Narrow", sans-serif; font-weight: 700;
    color: var(--title-yellow); font-size: 43px; line-height: 58px;
  }
  .front-photo {
    position: absolute; left: 46px; top: 403px; width: 495px; height: 301px;
    border: 5px solid var(--white);
    background:
      radial-gradient(ellipse 45% 40% at 55% 38%, var(--photo-glow), transparent 85%),
      radial-gradient(ellipse 90% 70% at 50% 45%, var(--photo-light), transparent 90%),
      linear-gradient(180deg, transparent 0%, transparent 70%, var(--photo-deep) 76%, var(--photo-edge) 86%, var(--photo-mid) 100%),
      linear-gradient(90deg, var(--photo-edge) 0%, var(--photo-light) 30%, var(--photo-light) 70%, var(--photo-edge) 100%);
  }
  .front-author {
    position: absolute; left: 0; width: 582px; top: 722px; text-align: center;
    font-family: "Arimo", Arial, sans-serif; font-size: 23px; color: var(--white);
  }
</style>
</head>
<body>
<main class="spread">
  <section class="back-cover">
    <div class="back-art" role="img" aria-label="Deep space photograph with a red nebula streak running diagonally across a starfield"></div>
    <div class="back-blurb">
      <h2>Abc defgh ijklmn :</h2>
      <p>opqrstu vwxyzA bc defgh<br>ijklmn, opqrs, tuvw xyz.<br>123456789 / 123456789</p>
    </div>
  </section>

  <section class="spine">
    <p class="spine-text">WALK BOLD STAY KIND : 47 Quiet Rules For Calm and Wonder</p>
    <p class="spine-text spine-author">By : A. B. Cdefghi</p>
  </section>

  <section class="front-cover">
    <div class="front-art" role="img" aria-label="Blue starry galaxy background"></div>
    <h1 class="front-title"><span>"WALK BOLD "</span><span>STAY KIND :</span></h1>
    <p class="front-subtitle">47 Quiet Rules For<br>Calm and Wonder</p>
    <div class="front-photo" role="img" aria-label="Photograph of a goldfish leaping out of a crowded fishbowl toward an empty bowl on a blue reflective surface"></div>
    <p class="front-author">By : A. B. Cdefghi</p>
  </section>
</main>
</body>
</html>
```